Business Card and Stationary for KVT Builders
Need standard business card, letterhead, and envelopes to incorporate our new logo
Business Card and Stationary for KVT Builders - Construction
Creative Brief
Simple
Rowan Pelley
Vice President
4621 Brantwell Houston, TX 77031
rowan@kvtbuilders.example
I'm open to layout ideas for all designs. letterhead and envelopes need to be accessible to incorporate microsoft office products.

```html
<!DOCTYPE html>
<html lang="en">
<head>
<meta charset="utf-8">
<title>KVT Builders – Business Card Concepts</title>
<link href="https://fonts.googleapis.com/css2?family=Arimo:wght@400;700&display=swap" rel="stylesheet">
<style>
  :root {
    --brand-blue: #3b3e9f;
    --card-white: #ffffff;
    --card-grey: #c9c9c9;
    --grey-light: #e6e6e6;
    --grey-dark: #b3b3b3;
    --divider: #9a9a9a;
    --sheet: #ffffff;
  }
  html, body {
    margin: 0;
    padding: 0;
    overflow: hidden;
  }
  body {
    width: 1200px;
    height: 682px;
    background: var(--sheet);
    position: relative;
    font-family: "Arimo", Arial, sans-serif;
  }
  .card {
    position: absolute;
    box-sizing: border-box;
    display: flex;
    align-items: center;
    justify-content: center;
  }
  .card--front-white { left: 10px; top: 10px; width: 302px; height: 326px; background: var(--card-white); border: 1px solid #ddd; }
  .card-divider { position: absolute; left: 312px; top: 10px; width: 4px; height: 326px; background: var(--divider); }
  .card--back-blue { left: 316px; top: 10px; width: 279px; height: 326px; background: var(--brand-blue); color: var(--card-white); display: block; }
  .card--front-gradient { left: 612px; top: 10px; width: 578px; height: 326px; background: radial-gradient(ellipse at center, var(--grey-light) 0%, var(--grey-dark) 100%); }
  .card--front-grey { left: 10px; top: 350px; width: 585px; height: 322px; background: var(--card-grey); border: 1px solid #aaa; }
  .card--front-blue { left: 612px; top: 350px; width: 578px; height: 322px; background: var(--brand-blue); }

  .wordmark {
    display: flex;
    align-items: center;
    gap: 12px;
    font-weight: 700;
    color: var(--brand-blue);
    white-space: nowrap;
  }
  .wordmark__square { background: var(--brand-blue); }
  .wordmark--small { font-size: 34px; }
  .wordmark--small .wordmark__square { width: 22px; height: 22px; }
  .wordmark--large { font-size: 62px; }
  .wordmark--large .wordmark__square { width: 40px; height: 40px; }
  .wordmark--reversed { color: var(--card-white); }
  .wordmark--reversed .wordmark__square { background: var(--card-white); }

  .contact-name { position: absolute; right: 24px; top: 18px; text-align: right; }
  .contact-name__name { font-size: 17px; font-weight: 700; }
  .contact-name__title { font-size: 13px; margin-top: 3px; }
  .contact-details { position: absolute; right: 24px; top: 170px; text-align: right; font-size: 13px; line-height: 1.45; }
</style>
</head>
<body>
  <section class="card card--front-white">
    <div class="wordmark wordmark--small"><span class="wordmark__square"></span>KVT Builders</div>
  </section>
  <div class="card-divider"></div>
  <section class="card card--back-blue">
    <div class="contact-name">
      <div class="contact-name__name">Rowan Pelley</div>
      <div class="contact-name__title">Vice President</div>
    </div>
    <address class="contact-details" style="font-style:normal">
      4621 Brantwell<br>
      Houston, TX 77031<br>
      Phone : (713) 555-0142<br>
      Cell : (713) 555-0187<br>
      Fax : (713) 555-0163<br>
      Email : rowan@kvtbuilders.example
    </address>
  </section>
  <section class="card card--front-gradient">
    <div class="wordmark wordmark--large"><span class="wordmark__square"></span>KVT Builders</div>
  </section>
  <section class="card card--front-grey">
    <div class="wordmark wordmark--large"><span class="wordmark__square"></span>KVT Builders</div>
  </section>
  <section class="card card--front-blue">
    <div class="wordmark wordmark--large wordmark--reversed"><span class="wordmark__square"></span>KVT Builders</div>
  </section>
</body>
</html>
```